Internal Office Slogans / Motto / Vision Statements

Hi. We would like to put up some posters around the office with quotations such as -
-”Do what you do so well that they will want to see it again and bring their friends.”- Harlan Pruett
-Make your customers feel heard and understood. Make your customers feel respected and liked. Make your customers feel appreciated and helped. Understand that you can do none of these things unless you are sincere about them.
Gordon Felsk
- It’s a very predictable and satisfying phenomenon: whenever we get better, our customers do too.
Ray Tolbin
-Catch people in the act of performing extraordinary customer service. Treat them like heroes. Tell their stories, far and wide.
Neil Hartcombe

The purpose of the posters is to reiterate our culture and vision within the organisation. They should be clean, crisp and eye catching, not gaudy or bright. Professional, bold and strong.

The company website and logo is at http://www.norvanta.com.au
Print size will be A1

Thanks for participating & looking forward to seeing your great work.
Updates

Hi All. . 

So to reiterate we are looking for one background design to be used for multiple quotes...  The list of quotes are as follows: 

Support and or Sales Office

 

Make your customers feel heard and understood.Make your customers feel respected and liked. Make your customers feelappreciated and helped. Understand that you can do none of these things unlessyou are sincere about them.

Gordon Felsk

 

Nothing liberates our greatness like the desireto help, the desire to serve

Rosalind Pevrell

 

It’s a very predictable and satisfying phenomenon:whenever we get better, our customers do too.

Ray Tolbin

 

Success means we go to sleep at night knowingthat our talents and abilities were used in a way that served others.

Rosalind Pevrell.

 

The sole purpose of business is to create, serveand satisfy a customer, from beginning to end – and that’s everyone’s job.

Neil Hartcombe

 

We don’t celebrate closing a sale, we celebrateopening a relationship.

Eleanor Quisk

I will never make you a promise – unless I giveyou a plan and procedure to make that promise possible.

Lon Borstad

 

Customers feel we take them for granted; onlyshow interest when we want an order; lavish our time on prospects; communicatemainly by invoice; are fixated on big accounts; drop them like hot potatoesonce we have the order; don’t follow through on promises; and satisfy our ownbureaucracy rather than their needs. We can do better than that, much better.

Peter K Almsby.

 

 

General and public area

 

Catch people in the act of performingextraordinary customer service. Treat them like heroes. Tell their stories, farand wide.

Neil Hartcombe

 

 

We see our customers as invited guests to aparty, and we are the hosts. It’s our job every day to make every importantaspect of the customer experience a little bit better." Carl Dunmore - Founder andCEO of Veltrona

 

"If you do build a great experience,customers tell each other about that. Word of mouth is verypowerful."  Carl Dunmore

 

It's not a faithin technology. It's faith in people. Frank Toller

 

“Being the richest man in the cemetery doesn’tmatter to me … Going to bed at night saying we’ve done something wonderful…that’s what matters to me.” Frank Toller

 

The customer experience is the next competitivebattleground. Terry Mandevic, CIO, Quorra Computers

 

”Do what you do so well that they will want tosee it again and bring their friends.”- Harlan Pruett

In the world of internet customer service, it isimportant to remember your competitor is only a mouse click away. GlennPirsley (not sure who he is but like the quote).

The customer is why you go to work. If they goaway, you do, too. Simon Largotti (?)

 

MaybeSome for Sales or Build Team:

Quality is remembered long after the price is forgotten. Renzoli Family Slogan

```html
<!DOCTYPE html>
<html lang="en">
<head>
<meta charset="utf-8">
<title>Norvanta — Office Quote Poster</title>
<link href="https://fonts.googleapis.com/css2?family=Arimo:ital,wght@0,700;1,400&display=swap" rel="stylesheet">
<style>
  :root {
    --knit-dark: #232d34;
    --knit-mid: #36424b;
    --knit-light: #3f4b54;
    --accent-red: #cc0000;
    --text-white: #ffffff;
  }
  html, body {
    margin: 0;
    padding: 0;
    width: 848px;
    height: 1200px;
    overflow: hidden;
    background: var(--knit-dark);
  }
  .poster {
    position: relative;
    width: 848px;
    height: 1200px;
    overflow: hidden;
    font-family: "Arimo", Arial, sans-serif;
  }
  .poster__texture {
    position: absolute;
    inset: 0;
    background:
      radial-gradient(ellipse at 50% 40%, var(--knit-light) 0%, var(--knit-mid) 45%, var(--knit-dark) 100%);
  }
  .brand {
    position: absolute;
    left: 63px;
    top: 53px;
    display: flex;
    align-items: center;
    gap: 10px;
  }
  .brand__square {
    width: 44px;
    height: 44px;
    background: var(--accent-red);
  }
  .brand__name {
    color: var(--text-white);
    font-weight: 700;
    font-size: 50px;
    line-height: 1;
    letter-spacing: -1px;
  }
  .quote-marks {
    position: absolute;
    inset: 0;
  }
  .quote {
    position: absolute;
    left: 129px;
    top: 406px;
    margin: 0;
    color: var(--text-white);
    font-weight: 700;
    font-size: 66px;
    line-height: 88px;
    letter-spacing: 0.5px;
  }
  .quote__author {
    position: absolute;
    left: 397px;
    top: 855px;
    color: var(--text-white);
    font-style: italic;
    font-size: 13px;
    line-height: 1;
  }
</style>
</head>
<body>
<main class="poster">
  <div class="poster__texture" role="img" aria-label="Dark charcoal knitted fabric texture background"></div>

  <header class="brand">
    <span class="brand__square"></span>
    <span class="brand__name">Norvanta</span>
  </header>

  <svg class="quote-marks" width="848" height="1200" viewBox="0 0 848 1200" aria-hidden="true">
    <defs>
      <path id="quote-mark" d="M0,183 L0,105 C0,55 32,14 88,0 L100,22 C72,38 60,62 60,88 L100,88 L100,183 Z"/>
    </defs>
    <g class="quote-marks__open" fill="var(--accent-red)">
      <use href="#quote-mark" x="73" y="357"/>
      <use href="#quote-mark" x="200" y="357"/>
    </g>
    <g class="quote-marks__close" fill="var(--accent-red)" transform="rotate(180 668 790)">
      <use href="#quote-mark" x="553" y="698"/>
      <use href="#quote-mark" x="680" y="698"/>
    </g>
  </svg>

  <blockquote class="quote">
    Nothing liberates<br>
    our greatness<br>
    like the desireto<br>
    help, the desire<br>
    to serve.
  </blockquote>
  <cite class="quote__author">Rosalind Pevrell</cite>
</main>
</body>
</html>
```